Luxury Jewellery Brand Business Card design
A website will be needed shortly after so show your skills
Luxury Jewellery Brand Business Card design  - Jewelry
Creative Brief
Simple
Marcus Delvecky
Creative Director
47D Westbury mansions Westbury place london sw3k 2rt
marcus@lorvanemora.com
www.lorvanemora.com
The phone number provided is for design purpose only the real phone number will replace the temp at the end of the competition
tobiasgrell tobiasgrell
Hello all designers!! I have been very impressed with all the entries so far. I would like to see your best versions with colour . The colors I like are royal puple,racing green ,Red and an all white version . I like grey too but must be a dark grey ... have a go ... Thanks
#10 try it all with the filled in logo
#3 like the size of the logo
Thanks.Your the first to upload Could you possibly try the card using Logo lorvanemora_logo2_47729.jpg that I have uploaded ?
hi guys , Good luck with this one !!!! I am looking for interesting business cards !! simple but memorable!!! Excited to see what you guys come up with.....

```html
<!DOCTYPE html>
<html lang="en">
<head>
<meta charset="utf-8">
<title>Lorvane Mora – Business Card</title>
<link rel="stylesheet" href="https://fonts.googleapis.com/css2?family=Cormorant+Garamond:wght@500&family=Didact+Gothic&display=swap">
<style>
  :root {
    --stage: #e9e7e4;
    --card-white: #ffffff;
    --ink: #111111;
    --ink-soft: #2b2b2b;
    --back-dark: #0c0c0c;
    --back-mid: #262626;
    --reverse: #ffffff;
  }
  * { margin: 0; padding: 0; box-sizing: border-box; }
  html, body {
    width: 1200px; height: 901px; overflow: hidden;
    background: var(--stage);
  }
  .canvas { position: relative; width: 1200px; height: 901px; }

  .card {
    position: absolute;
    width: 620px; height: 354px;
    box-shadow: 0 10px 28px rgba(0,0,0,0.18);
  }

  /* Reverse side */
  .card--back {
    left: 60px; top: 70px;
    background: var(--back-dark);
    overflow: hidden;
  }
  .back-pattern {
    position: absolute; inset: 0;
    background: radial-gradient(circle at 35% 40%, var(--back-mid), var(--back-dark) 75%);
  }
  .back-brand {
    position: absolute; right: 60px; top: 150px;
    font-family: "Cormorant Garamond", serif;
    font-weight: 500; font-size: 20px; letter-spacing: 3px;
    color: var(--reverse);
  }

  /* Front side */
  .card--front {
    left: 520px; top: 470px;
    background: var(--card-white);
    color: var(--ink);
    overflow: hidden;
    font-family: "Didact Gothic", sans-serif;
  }
  .brand {
    position: absolute; left: 58px; top: 48px;
    display: flex; flex-direction: column; align-items: center; gap: 8px;
  }
  .brand-mark {
    width: 26px; height: 26px; background: var(--ink);
  }
  .brand-name {
    font-family: "Cormorant Garamond", serif;
    font-weight: 500; font-size: 34px; letter-spacing: 2px;
    line-height: 1; color: var(--ink);
  }
  .person { position: absolute; left: 60px; top: 140px; }
  .person-name { font-size: 17px; font-weight: 700; color: var(--ink); }
  .person-role { font-size: 12px; color: var(--ink-soft); margin-top: 3px; }
  .address {
    position: absolute; left: 60px; top: 195px;
    font-size: 12px; line-height: 1.45; color: var(--ink-soft);
  }
  .contacts {
    position: absolute; left: 48px; top: 244px;
    list-style: none; font-size: 12px; color: var(--ink-soft);
  }
  .contacts li { display: flex; align-items: center; gap: 7px; height: 17px; }
  .contacts svg { width: 11px; height: 11px; fill: var(--ink); flex: none; }

  .brand-large {
    position: absolute; right: 24px; bottom: 26px;
    text-align: right;
    font-family: "Cormorant Garamond", serif;
    font-weight: 500; font-size: 64px; line-height: 0.95;
    letter-spacing: 2px; color: var(--ink);
  }
</style>
</head>
<body>
<main class="canvas">

  <section class="card card--back">
    <div class="back-pattern" role="img" aria-label="Repeating black-on-black geometric jewellery motif pattern"></div>
    <span class="back-brand">LORVANE MORA</span>
  </section>

  <section class="card card--front">
    <div class="brand">
      <span class="brand-mark"></span>
      <span class="brand-name">LORVANE MORA</span>
    </div>

    <div class="person">
      <p class="person-name">Marcus Delvecky</p>
      <p class="person-role">Creative Director</p>
    </div>

    <p class="address">47D Westbury Mansions Westbury<br>Place London SW3K 2RT</p>

    <ul class="contacts">
      <li>
        <svg viewBox="0 0 12 12"><path d="M1 3c0-1 1-2 2-2h6c1 0 2 1 2 2v1H8V3H4v1H1zM2 5h8l1 6H1z"/></svg>
        0044 203 555 0142
      </li>
      <li>
        <svg viewBox="0 0 12 12"><path d="M3 0h6v12H3zM4 1.5v8h4v-8z"/></svg>
        0044 7700 900 318
      </li>
      <li>
        <svg viewBox="0 0 12 12"><path d="M0 2h12v8H0zM1 3l5 4 5-4v-.2H1z"/></svg>
        marcus@lorvanemora.com
      </li>
      <li>
        <svg viewBox="0 0 12 12"><path d="M6 0a6 6 0 1 0 0 12A6 6 0 0 0 6 0zm0 1.5a4.5 4.5 0 1 1 0 9 4.5 4.5 0 0 1 0-9z"/></svg>
        www.lorvanemora.com
      </li>
    </ul>

    <div class="brand-large">LORVANE<br>MORA</div>
  </section>

</main>
</body>
</html>
```